Modern Billboard Ad for Criminal Defense Firm

10.5 x 36 We're looking for something to set us apart from the local competition. Looking for sleek and modern. We're a mid-sized firm in a small market city. We want to give the artist room to be creative on this one.
Thanks

Target Market(s)

Adult clients who have been charged with a crime/DWI

Industry/Entity Type

legal

Font styles to use
Serif
Sans Serif

Requirements
Must have
• Needs to have the firm name in large lettering. Law Offices of Marcus T Whitfield. “PLLC” does not have to be included. Phone number of (555) 384-1927 should be included but not the main focus.
Nice to have
• A call to action or something similar. “Don’t go it alone, call today.”, “ Arrested?”

```html
<!DOCTYPE html>
<html lang="en">
<head>
<meta charset="utf-8">
<title>Law Offices of Marcus T Whitfield – Billboard</title>
<link rel="stylesheet" href="https://fonts.googleapis.com/css2?family=Gelasio:wght@500;700&display=swap">
<style>
  :root {
    --page: #ffffff;
    --board: #070707;
    --board-edge: #1a1a1a;
    --accent: #05aaee;
    --text-light: #ffffff;
    --portrait-dark: #2b2b2d;
    --portrait-mid: #7d7b78;
    --badge-fill: #222326;
  }
  * { margin: 0; padding: 0; box-sizing: border-box; }
  html, body {
    width: 1200px;
    height: 712px;
    overflow: hidden;
    background: var(--page);
  }
  .canvas {
    position: relative;
    width: 1200px;
    height: 712px;
  }
  .billboard {
    position: absolute;
    left: 123px;
    top: 216px;
    width: 913px;
    height: 266px;
    background: radial-gradient(ellipse at 45% 55%, #141414 0%, var(--board) 70%);
    border: 1px solid var(--board-edge);
    overflow: hidden;
    font-family: "Gelasio", Georgia, serif;
  }
  .attorney-portrait {
    position: absolute;
    left: 740px;
    top: 18px;
    width: 173px;
    height: 248px;
    z-index: 1;
    background: linear-gradient(180deg, var(--board) 0%, var(--board) 30%, var(--portrait-dark) 50%, var(--portrait-mid) 100%);
  }
  .firm-name {
    position: absolute;
    left: 427px;
    top: 64px;
    z-index: 2;
    transform: translateX(-50%);
    white-space: nowrap;
    color: var(--text-light);
    font-weight: 700;
    font-size: 35px;
    line-height: 1;
    letter-spacing: -0.2px;
  }
  .phone {
    position: absolute;
    left: 432px;
    top: 131px;
    z-index: 2;
    transform: translateX(-50%);
    white-space: nowrap;
    color: var(--accent);
    font-weight: 700;
    font-size: 42px;
    line-height: 1;
    font-variant-numeric: lining-nums;
  }
  .cta-band {
    position: absolute;
    left: 0;
    top: 226px;
    width: 740px;
    height: 40px;
    background: var(--accent);
  }
  .cta-text {
    position: absolute;
    left: 425px;
    top: 230px;
    z-index: 2;
    transform: translateX(-50%);
    white-space: nowrap;
    color: var(--text-light);
    font-weight: 700;
    font-size: 24px;
    line-height: 1.3;
  }
  .award-badge {
    position: absolute;
    left: 1px;
    top: 112px;
    width: 93px;
    height: 114px;
    background: linear-gradient(180deg, var(--accent) 0%, var(--accent) 28%, var(--badge-fill) 28%);
    border: 2px solid var(--accent);
  }
</style>
</head>
<body>
  <main class="canvas">
    <section class="billboard">
      <div class="attorney-portrait" role="img" aria-label="Portrait photo of the attorney in a grey plaid suit and blue tie"></div>
      <h1 class="firm-name">Law Offices of Marcus T Whitfield</h1>
      <p class="phone">(555) 384-1927</p>
      <div class="cta-band"></div>
      <p class="cta-text">Don’t go it alone, call today</p>
      <div class="award-badge" role="img" aria-label="Community choice award badge"></div>
    </section>
  </main>
</body>
</html>
```